Heads Up Display for In-Car racing video PSD

I need my in-car racing video overlay converted to a heads up digital display. The elements that need to be included in the display are the speedometer, odometer (rpms), accelerometer (that is the circle graphic found on the attached example called "current video overlay"), the track map, the current lap time, and the best lap time. We also need to include the attached logo in the top right corner of the display as well as the interior shot of the cockpit on the top left corner of the display. These elements can be found on the attachment called "current video overlay".
The final delivered file must be a PSD (Photoshop Document) with layers for all of the above elements. Attached is our company font as well as the digital font to use for the gauges for the design. Also attached is our company logo for the display, an example of our current video player and an example of the style we want the new one to look like.
Color Scheme for heads up display:
You may use a combination of these colors for the design:
#ffbf3f
#222222
#ffffff
#b0b0b0
Industry/Entity Type
Car Racing
Requirements
Must have
- Heads Up Display should have partial transparency so you can see the track through it.
- Must look exciting and race car inspired

```html
<!DOCTYPE html>
<html lang="en">
<head>
<meta charset="utf-8">
<title>TrackRush In-Car HUD</title>
<link rel="stylesheet" href="https://fonts.googleapis.com/css2?family=Michroma&family=Orbitron:wght@500&family=Saira+Condensed:wght@500&display=swap">
<style>
  :root {
    --amber: #ffbf3f;
    --ink: #222222;
    --white: #ffffff;
    --grey: #b0b0b0;
    --page: #ffffff;
  }
  * { margin: 0; padding: 0; box-sizing: border-box; }
  html, body { width: 1200px; height: 635px; overflow: hidden; background: var(--page); }
  .canvas { position: relative; width: 1200px; height: 635px; }
  .frame { position: absolute; left: 12px; top: 12px; width: 1176px; height: 610px; overflow: hidden; }
  .track-view {
    position: absolute; inset: 0;
    background: linear-gradient(180deg,
      #b9c3c9 0%, #cfd4d4 25%, #aeb3b6 36%,
      #6b6d52 42%, #7a7460 58%, #8f8677 70%,
      #2a2a2a 78%, #1c1c1c 100%);
  }
  .top-band {
    position: absolute; left: 366px; right: 0; top: 0; height: 62px;
    background: linear-gradient(90deg, rgba(34,34,34,0) 0%, rgba(34,34,34,.55) 100%);
  }
  .brand {
    position: absolute; right: 16px; top: 14px;
    font-family: "Michroma", sans-serif; font-size: 34px; letter-spacing: 1px;
    color: var(--white); line-height: 1;
  }
  .cockpit-cam {
    position: absolute; left: 0; top: 0; width: 366px; height: 182px;
    border: 3px solid var(--ink);
    background: linear-gradient(135deg, #2b2b2b 0%, #5a5e5c 45%, #3b4a3c 70%, #1d1d1d 100%);
  }
  .hud { position: absolute; inset: 0; }
  .hud svg { position: absolute; left: 0; top: 0; }
  .label {
    position: absolute; font-family: "Saira Condensed", sans-serif; font-weight: 500;
    color: var(--white); font-size: 15px; line-height: 1; letter-spacing: .5px;
  }
  .digits {
    position: absolute; font-family: "Orbitron", sans-serif; font-weight: 500;
    color: var(--amber); line-height: 1;
  }
  .lap-label { left: 30px; top: 420px; }
  .lap-time { left: 30px; top: 440px; font-size: 21px; }
  .best-label { left: 360px; top: 420px; width: 82px; text-align: right; }
  .best-time { left: 328px; top: 440px; font-size: 21px; width: 114px; text-align: right; }
  .rpm-value { left: 56px; top: 514px; font-size: 17px; }
  .rpm-unit { left: 112px; top: 547px; font-size: 9px; }
  .speed-value { left: 176px; top: 492px; font-size: 46px; }
  .speed-unit { left: 296px; top: 500px; font-size: 10px; }
  .speed-unit.per { top: 515px; }
  .track-map {
    position: absolute; left: 1054px; top: 408px; width: 72px; height: 182px;
    border: 2px solid rgba(255,255,255,.8); border-radius: 8px;
    background: rgba(255,255,255,.12);
  }
</style>
</head>
<body>
<div class="canvas">
  <div class="frame">
    <div class="track-view" role="img" aria-label="Driver's-eye view down a straight desert road with a yellow centre line, mountains ahead and the car's dashboard in the foreground"></div>
    <div class="top-band"></div>
    <div class="brand">TRACKRUSH</div>
    <div class="cockpit-cam" role="img" aria-label="Interior camera shot of the helmeted driver in the cockpit"></div>

    <div class="hud">
      <svg width="1176" height="610" viewBox="0 0 1176 610" fill="none">
        <g class="lap-rule" stroke="var(--white)" stroke-width="2">
          <polyline points="30,410 132,410 156,432"/>
          <polyline points="316,432 340,410 442,410"/>
        </g>
        <g class="rpm-gauge">
          <circle cx="90" cy="522" r="34" fill="rgba(176,176,176,.35)"/>
          <path d="M50,474 A60,60 0 0 1 150,484" stroke="var(--white)" stroke-width="2"/>
          <path d="M34,540 A60,60 0 0 0 70,578" stroke="var(--white)" stroke-width="2"/>
          <line x1="56" y1="500" x2="126" y2="500" stroke="var(--grey)" stroke-width="2"/>
          <line x1="56" y1="562" x2="126" y2="562" stroke="var(--grey)" stroke-width="2"/>
        </g>
        <g class="speed-gauge">
          <circle cx="236" cy="512" r="52" fill="rgba(176,176,176,.35)"/>
          <path d="M196,432 A92,92 0 0 1 310,440" stroke="var(--white)" stroke-width="2"/>
          <path d="M160,454 A92,92 0 0 0 210,600" stroke="var(--white)" stroke-width="2"/>
          <line x1="180" y1="468" x2="296" y2="468" stroke="var(--grey)" stroke-width="2"/>
          <line x1="180" y1="566" x2="296" y2="566" stroke="var(--grey)" stroke-width="2"/>
        </g>
        <g class="accelerometer" stroke="var(--white)" stroke-width="2">
          <circle cx="388" cy="524" r="54" fill="rgba(34,34,34,.25)"/>
          <circle cx="388" cy="524" r="40"/>
          <circle cx="388" cy="524" r="26"/>
          <circle cx="388" cy="524" r="13"/>
          <circle cx="394" cy="534" r="6" fill="var(--amber)" stroke="none"/>
        </g>
      </svg>

      <div class="label lap-label">LAP 1</div>
      <div class="digits lap-time">00:08.23</div>
      <div class="label best-label">BEST LAP</div>
      <div class="digits best-time">05:34.23</div>
      <div class="digits rpm-value">05320</div>
      <div class="label rpm-unit">/RPM</div>
      <div class="digits speed-value">090</div>
      <div class="label speed-unit">MILES</div>
      <div class="label speed-unit per">/HOUR</div>
      <div class="track-map" role="img" aria-label="Track map outline with the car's current position marked"></div>
    </div>
  </div>
</div>
</body>
</html>
```